Business Card Design Project

We're looking for a unique business card design that stands out from the rest, using the brand and logo we've already developed.
Two-sided design please.
Vantor Creative (www.vantorcreative.example.au) is a digitally-focused advertising agency that has produces results-driven campaigns. As a result, we'd like our business card to reflect our innovative approach.
Size, shape, orientation, etc, are all flexible (providing the print costs don't become ridiculous or we have to sit there with tiny scissors!).
Business card should include space for name, title, email, mobile, landline and address.

```html
<!DOCTYPE html>
<html lang="en">
<head>
<meta charset="utf-8">
<title>Vantor Creative – Business Cards</title>
<link rel="stylesheet" href="https://fonts.googleapis.com/css2?family=Montserrat:wght@300;400;600;700&display=swap">
<style>
  :root {
    --backdrop: #2b2623;
    --card: #1b1b1b;
    --ink: #f2f2f2;
    --ink-soft: #cfcfcf;
    --accent: #f7871e;
  }
  * { box-sizing: border-box; margin: 0; padding: 0; }
  html, body { width: 1200px; height: 716px; overflow: hidden; }
  body {
    background: var(--backdrop);
    font-family: "Montserrat", Arial, sans-serif;
    color: var(--ink);
    position: relative;
  }
  .card {
    position: absolute;
    top: 208px;
    width: 520px;
    height: 300px;
    background: var(--card);
    box-shadow: 0 10px 30px rgba(0,0,0,.45);
  }
  .card--services { left: 50px; }
  .card--contact { left: 630px; }

  /* services side */
  .services {
    position: absolute;
    left: 30px; right: 30px; top: 56px;
    text-align: center;
    line-height: 1.55;
    font-weight: 300;
  }
  .services p { font-size: 14px; white-space: nowrap; }
  .services b { font-weight: 700; }
  .services .hl { color: var(--accent); }
  .services .gap { display: inline-block; width: 36px; }
  .services .big { font-size: 20px; margin-top: 2px; }
  .edge-stripe {
    position: absolute; right: 0; top: 0; width: 5px; height: 100%;
    background: var(--accent);
  }
  .brand-small {
    position: absolute; right: 22px; bottom: 16px;
    font-size: 10px; font-weight: 400; color: var(--ink);
  }

  /* contact side */
  .brand {
    position: absolute; right: 36px; top: 60px;
    font-size: 28px; font-weight: 300; color: var(--ink); letter-spacing: 1px;
  }
  .name-bar {
    position: absolute; left: 0; top: 100px; width: 6px; height: 34px;
    background: var(--accent);
  }
  .person { position: absolute; left: 26px; top: 100px; }
  .person .name { font-size: 18px; font-weight: 400; }
  .person .title { font-size: 12px; font-weight: 600; color: var(--accent); margin-left: 28px; }
  .contacts {
    position: absolute; left: 14px; top: 166px; list-style: none;
    font-size: 14px; line-height: 19px;
  }
  .contacts li { display: flex; align-items: center; gap: 10px; }
  .contacts svg { width: 12px; height: 12px; fill: var(--accent); flex: none; }
  .side-bar { position: absolute; right: 0; width: 6px; background: var(--accent); }
  .side-bar--top { top: 94px; height: 20px; }
  .side-bar--bottom { top: 140px; height: 130px; }
</style>
</head>
<body>
  <section class="card card--services">
    <div class="services">
      <p>Campaign Analytics, <b>Tracking</b> and <b class="hl">Reporting</b></p>
      <p><b>Web Usability</b> <span class="hl">and</span> <b>Consulting</b></p>
      <p>Conversion <b>Optimisation</b><span class="gap"></span><b>Search Engine Optimisation</b></p>
      <p>Pay Per Click <b class="hl">Advertising</b></p>
      <p class="big">Social <b class="hl">Media</b> Marketing</p>
    </div>
    <span class="brand-small">Vantor Creative</span>
    <span class="edge-stripe"></span>
  </section>

  <section class="card card--contact">
    <span class="brand">Vantor Creative</span>
    <span class="name-bar"></span>
    <div class="person">
      <p class="name">Sample Name</p>
      <p class="title">title</p>
    </div>
    <ul class="contacts">
      <li><svg viewBox="0 0 12 12"><path d="M0 2h12v8H0z M0 2l6 5 6-5" /></svg>youremailaddress@example.com</li>
      <li><svg viewBox="0 0 12 12"><path d="M2 1h3l1 3-2 1a7 7 0 0 0 3 3l1-2 3 1v3c-6 1-10-3-9-9z"/></svg>+61 400 555 019</li>
      <li><svg viewBox="0 0 12 12"><path d="M6 0a4 4 0 0 1 4 4c0 3-4 8-4 8S2 7 2 4a4 4 0 0 1 4-4zm0 2.5a1.5 1.5 0 1 0 0 3 1.5 1.5 0 0 0 0-3z"/></svg>Sample address</li>
    </ul>
    <span class="side-bar side-bar--top"></span>
    <span class="side-bar side-bar--bottom"></span>
  </section>
</body>
</html>
```